Letterhead to coordinate with business card

I am needing a docx template and print file for a letterhead to co-ordinate with my newly designed logo and business card.

```html
<!DOCTYPE html>
<html lang="en">
<head>
<meta charset="utf-8">
<title>Tidewell Plan Management – Letterhead</title>
<link href="https://fonts.googleapis.com/css2?family=Arimo:wght@400&family=Mulish:wght@700&display=swap" rel="stylesheet">
<style>
  :root {
    --backdrop: #acaaab;
    --paper: #ffffff;
    --magenta: #a93065;
    --teal: #00807f;
    --ink: #4a4a4a;
    --ink-dark: #333333;
  }
  html, body {
    margin: 0;
    padding: 0;
    width: 1200px;
    height: 934px;
    overflow: hidden;
    background: var(--backdrop);
  }
  .letterhead {
    position: absolute;
    left: 322px;
    top: 74px;
    width: 556px;
    height: 786px;
    background: var(--paper);
    overflow: hidden;
    font-family: "Arimo", Arial, sans-serif;
    color: var(--ink);
  }
  .brand {
    position: absolute;
    left: 44px;
    top: 34px;
    width: 126px;
    text-align: center;
  }
  .brand-mark {
    display: block;
    width: 44px;
    height: 44px;
    margin: 0 auto 7px;
    background: var(--magenta);
  }
  .brand-name {
    margin: 0;
    font-family: "Mulish", Arial, sans-serif;
    font-weight: 700;
    color: var(--magenta);
    font-size: 13px;
    line-height: 15px;
    letter-spacing: 0.5px;
  }
  .address {
    position: absolute;
    right: 231px;
    top: 52px;
    margin: 0;
    font-style: normal;
    text-align: right;
    font-size: 9.4px;
    line-height: 11.4px;
    color: var(--ink-dark);
  }
  .divider {
    position: absolute;
    left: 334px;
    top: 49px;
    width: 0.7px;
    height: 30px;
    background: var(--ink-dark);
  }
  .contacts {
    position: absolute;
    left: 341px;
    top: 46px;
    margin: 0;
    padding: 0;
    list-style: none;
    font-size: 9.4px;
    line-height: 11.4px;
    color: var(--ink-dark);
  }
  .contacts li {
    display: flex;
    align-items: center;
    gap: 3px;
  }
  .contacts svg {
    width: 8px;
    height: 8px;
    flex: none;
  }
  .salutation {
    position: absolute;
    left: 50px;
    top: 240px;
    margin: 0;
    font-family: "Mulish", Arial, sans-serif;
    font-weight: 700;
    font-size: 13px;
    color: var(--ink);
  }
  .body-copy {
    position: absolute;
    left: 50px;
    top: 277px;
    width: 456px;
  }
  .body-copy p {
    margin: 0 0 10px;
    font-size: 9.5px;
    line-height: 11.4px;
  }
  .closing {
    position: absolute;
    left: 50px;
    top: 513px;
    margin: 0;
    font-family: "Mulish", Arial, sans-serif;
    font-weight: 700;
    font-size: 7.5px;
    color: var(--ink);
  }
  .signature {
    position: absolute;
    left: 50px;
    top: 546px;
    width: 91px;
    height: 28px;
    background: linear-gradient(90deg, #e4e4e4, #d2d2d2);
  }
  .footer-band {
    position: absolute;
    left: 0;
    bottom: 0;
    width: 556px;
    height: 44px;
    background: linear-gradient(90deg, var(--magenta), var(--teal) 60%);
  }
</style>
</head>
<body>
  <main class="letterhead">
    <header>
      <div class="brand">
        <span class="brand-mark"></span>
        <p class="brand-name">TIDEWELL<br>Plan Management</p>
      </div>

      <address class="address">PO Box 240<br>Lakeview NSW 2400</address>
      <span class="divider"></span>

      <ul class="contacts">
        <li>
          <svg viewBox="0 0 10 10" aria-hidden="true"><circle cx="5" cy="5" r="5" fill="var(--teal)"/><path d="M3.2 2.6c.3-.2.6-.1.8.2l.4.7c.1.3 0 .5-.2.6l-.3.2c.2.6.7 1.1 1.3 1.4l.2-.3c.2-.2.4-.3.6-.2l.7.4c.3.2.4.5.2.8-.3.5-.8.7-1.4.5C4.3 6.5 3.4 5.6 3 4.3c-.2-.6 0-1.3.2-1.7z" fill="#fff"/></svg>
          <span>0400 123 456</span>
        </li>
        <li>
          <svg viewBox="0 0 10 10" aria-hidden="true"><circle cx="5" cy="5" r="5" fill="var(--teal)"/><rect x="2.6" y="3.3" width="4.8" height="3.4" fill="none" stroke="#fff" stroke-width=".7"/><path d="M2.6 3.3 5 5.2l2.4-1.9" fill="none" stroke="#fff" stroke-width=".7"/></svg>
          <span>hello@tidewellplan.com.au</span>
        </li>
        <li>
          <svg viewBox="0 0 10 10" aria-hidden="true"><circle cx="5" cy="5" r="5" fill="var(--teal)"/><circle cx="5" cy="5" r="2.6" fill="none" stroke="#fff" stroke-width=".6"/><path d="M2.4 5h5.2M5 2.4c-1 1.4-1 3.8 0 5.2M5 2.4c1 1.4 1 3.8 0 5.2" fill="none" stroke="#fff" stroke-width=".5"/></svg>
          <span>www.tidewellplan.com.au</span>
        </li>
      </ul>
    </header>

    <h1 class="salutation">Dear Mr. Carter,</h1>

    <section class="body-copy">
      <p>Lorem ipsum dolor sit amet, consectetuer adipiscing elit, sed diam nonmmy nibh euismod tincidunt ut laor eet dolore magna aliquam erat volutpat. Ut wisi enim ad minim veniam, quis nostrud exerci tationmcorper suscipit lobortis nisl ut aliquip ex ea commodo consequat. Duis autem vel eum iriure dolor in hendrerit in vulputate velit esse molestie consequat, vel illum dolore eu feugiat</p>
      <p>Rorem ipsum dolor sit amet, consectetuer adipiscing elit, sed diam nonmmy nibh euismod tincidunt ut laor eet dolore magna aliquam erat volutpat. Ut wisi enim ad minim veniam, quis nostrud exerci tationmcorper suscipit lobortis nisl ut aliquip ex ea commodo consequat. Duis autem vel eum iriure dolor in hendrerit in vulputate velit esse molest</p>
      <p>Dorem ipsum dolor sit amet, consectetuer adipiscing elit, sed diam nonmmy nibh euismod tincidunt ut laor eet dolore magna aliquam erat volutpat. Ut wisi enim ad minim veniam, quis nostrud exerci tationmcorper suscipit lobortis nisl ut aliquip ex ea commodo consequat. Duis autem vel eum iriure dolor in hendrerit in suscipit lobortis nisl ut aliquip ex ea commodo consequat. Duis autem vel eum iriure dolor in hendrerit in vulputate velit esse molestie consequat, vel illum</p>
      <p>Sorem ipsum dolor sit amet, consectetuer adipiscing elit, sed diam nonmmy nibh euismod tincidunt ut laor eet dolore magna aliquam erat volutpat. Ut wisi enim ad minim veniam, quis nostrud exerci tationmcorper suscipit lobortis nisl ut aliquip ex ea commodo consequat. Duis autem vel eum iriure dolor in</p>
    </section>

    <p class="closing">Sincerely,</p>
    <div class="signature" role="img" aria-label="Handwritten signature of the sender"></div>

    <div class="footer-band" role="img" aria-label="Decorative footer band in magenta and teal"></div>
  </main>
</body>
</html>
```